K7 Business Card Design for Professional IT Security Company

I have a small Cyber Security Startup and I need to have a business card designed.

My company specializes in: Government Risk Compliance, Cyber Security Assessments, Big Data

Please use my logo and fonts attached.

Industry/Entity Type

Information Technology

Contact Information for Business Card

Details
Dale Whitcombe, MS, CISSP
Member
(p) 303.518.9046
(e) dwhitcombe@k7nexwavesys.net
(a) P.O. Box 587, Kelford, VA 22846

K7 Nexwave Systems
www.k7nexwavesys.net

Font styles to use
Other font styles liked:
• Please see attached

```html
<!DOCTYPE html>
<html lang="en">
<head>
<meta charset="utf-8">
<title>K7 Nexwave Systems – Business Card</title>
<link rel="stylesheet" href="https://fonts.googleapis.com/css2?family=Raleway:wght@300;400;500&display=swap">
<style>
  :root {
    --brand-blue: #0d5a9e;
    --brand-cyan: #2fb4e0;
    --ink-grey: #6b6f74;
    --rule-grey: #c9ccd0;
    --card-white: #fbfbfb;
    --backdrop: #ececec;
  }
  * { box-sizing: border-box; margin: 0; padding: 0; }
  html, body {
    width: 1200px; height: 885px; overflow: hidden;
    background: var(--backdrop);
    font-family: "Raleway", Arial, sans-serif;
  }
  .sheet {
    width: 1200px; height: 885px;
    display: flex; align-items: center; justify-content: center; gap: 60px;
  }
  .card {
    width: 520px; height: 297px; position: relative; overflow: hidden;
    box-shadow: 0 2px 6px rgba(0,0,0,0.12);
  }

  /* Front */
  .card-front { background: var(--card-white); }
  .holder { position: absolute; left: 38px; top: 56px; }
  .holder-name {
    font-size: 25px; font-weight: 400; letter-spacing: 0.5px;
    color: var(--brand-blue); text-transform: uppercase;
  }
  .holder-name .credentials { font-size: 17px; }
  .holder-role {
    margin-top: 4px; font-size: 11px; letter-spacing: 1.5px;
    color: var(--brand-cyan); text-transform: uppercase;
  }
  .contact { position: absolute; left: 38px; top: 132px; color: var(--ink-grey); font-size: 10.5px; }
  .contact-address { margin-bottom: 6px; }
  .contact-line { display: flex; align-items: center; gap: 6px; white-space: nowrap; }
  .contact-line svg { width: 11px; height: 11px; flex: none; }
  .contact-line .divider { color: var(--rule-grey); }
  .company-mark {
    position: absolute; right: 34px; top: 104px;
    display: flex; align-items: center; gap: 8px;
  }
  .company-mark .dot { width: 12px; height: 12px; background: var(--brand-blue); }
  .company-mark .name {
    font-size: 15px; font-weight: 500; color: var(--brand-blue);
    text-transform: uppercase; letter-spacing: 1px; line-height: 1.2; width: 110px;
  }
  .rule { position: absolute; left: 38px; right: 34px; top: 210px; height: 1px; background: var(--rule-grey); }
  .base-band { position: absolute; left: 0; right: 0; bottom: 44px; height: 5px; display: flex; align-items: center; }
  .base-band .band-blue { width: 56%; height: 5px; background: var(--brand-blue); }
  .base-band .band-cyan { width: 18%; height: 5px; background: var(--brand-cyan); }
  .base-band .band-grey { flex: 1; height: 1px; background: var(--rule-grey); }

  /* Back */
  .card-back {
    background: var(--brand-blue);
    display: flex; flex-direction: column; align-items: center; justify-content: center;
  }
  .back-mark {
    display: flex; align-items: center; gap: 10px;
    font-size: 22px; font-weight: 500; color: #ffffff;
    text-transform: uppercase; letter-spacing: 1.5px;
  }
  .back-mark .dot { width: 14px; height: 14px; background: #ffffff; }
  .services {
    margin-top: 26px; font-size: 9.5px; font-weight: 300; letter-spacing: 1px;
    color: #ffffff; text-transform: uppercase;
  }
</style>
</head>
<body>
<main class="sheet">
  <section class="card card-front" aria-label="Business card front">
    <div class="holder">
      <h1 class="holder-name">Dale Whitcombe, <span class="credentials">MS, CISSP</span></h1>
      <p class="holder-role">Member</p>
    </div>
    <div class="contact">
      <p class="contact-address">P.O. Box 587, Kelford, VA 22846</p>
      <p class="contact-line">
        <svg viewBox="0 0 12 12" aria-hidden="true"><path d="M2.5 1h2l1 2.5-1.3 1a6 6 0 0 0 3.3 3.3l1-1.3L11 7.5v2a1.3 1.3 0 0 1-1.4 1.3A9 9 0 0 1 1.2 2.4 1.3 1.3 0 0 1 2.5 1z" fill="#6b6f74"/></svg>
        <span>303.518.9046</span><span class="divider">|</span>
        <svg viewBox="0 0 12 12" aria-hidden="true"><rect x="1" y="2.5" width="10" height="7" fill="none" stroke="#6b6f74"/><path d="M1 2.5l5 4 5-4" fill="none" stroke="#6b6f74"/></svg>
        <span>dwhitcombe@k7nexwavesys.net</span><span class="divider">|</span>
        <svg viewBox="0 0 12 12" aria-hidden="true"><circle cx="6" cy="6" r="5" fill="none" stroke="#6b6f74"/><ellipse cx="6" cy="6" rx="2.2" ry="5" fill="none" stroke="#6b6f74"/><path d="M1 6h10" stroke="#6b6f74"/></svg>
        <span>www.k7nexwavesys.net</span>
      </p>
    </div>
    <div class="company-mark">
      <span class="dot"></span>
      <span class="name">K7 Nexwave Systems</span>
    </div>
    <div class="rule"></div>
    <div class="base-band"><span class="band-blue"></span><span class="band-cyan"></span><span class="band-grey"></span></div>
  </section>

  <section class="card card-back" aria-label="Business card back">
    <div class="back-mark"><span class="dot"></span><span>K7 Nexwave Systems</span></div>
    <p class="services">GRC • Pen Testing • Cloud Security • Big Data</p>
  </section>
</main>
</body>
</html>
```